New Website design for VelvetCrate.com - A Monthly Subscription Sexy Lingerie Biz

Look at these sites: https://www.quillrazorguild.com; http://www.parcelwardrobe.com; http://www.tinyfernpack.com; https://www.ochreladle.com; https://thegoldenradish.com; http://www.petalwickcrate.com; https://wagtote.com; https://www.marlowehush.com/coral

Industry/Entity Type

Lingerie

Coding

Coded - Design and coding required

Number of Pages Required

1 page

```html
<!DOCTYPE html>
<html lang="en">
<head>
<meta charset="utf-8">
<title>VelvetCrate – Lingerie Online Store</title>
<link href="https://fonts.googleapis.com/css2?family=Playfair+Display:wght@400;700;900&family=Roboto:wght@300;400;500;700&family=Open+Sans:wght@600;800&display=swap" rel="stylesheet">
<style>
:root{
  --teal:#15b39b;
  --red:#e2374a;
  --dark:#2b2b2b;
  --footer:#353535;
  --page:#ececec;
  --line:#ececec;
  --ink:#444;
  --muted:#9a9a9a;
  --star:#f5a623;
  --fb:#3b5998;--tw:#3fcdf5;--gr:#6ab514;--rd:#d53a2a;
}
*{box-sizing:border-box;margin:0;padding:0}
html,body{width:1200px;height:2954px;overflow:hidden}
body{background:var(--page);font-family:'Roboto',sans-serif;color:var(--ink);position:relative}
.abs{position:absolute}
/* top bar */
.topbar{left:0;top:0;width:1200px;height:31px;background:var(--dark)}
.topbar .welcome{left:157px;top:10px;font:10px 'Playfair Display',serif;color:#ddd}
.topbar .welcome b{color:#fff;font-weight:700}
.topbar .menu{top:10px;font:9px 'Playfair Display',serif;color:#ccc;letter-spacing:.3px}
.topbar .sep{top:7px;width:1px;height:17px;background:#555}
.cart{left:913px;top:0;width:133px;height:31px;background:var(--teal);color:#fff}
.cart .t1{position:absolute;left:42px;top:4px;font:700 9px 'Playfair Display',serif}
.cart .t2{position:absolute;left:42px;top:16px;font:8px 'Playfair Display',serif}
.cart svg{position:absolute;left:12px;top:6px}
/* header */
.header{left:0;top:31px;width:1200px;height:78px;background:#fff}
.logo{left:157px;top:20px}
.logo .name{font:700 25px 'Playfair Display',serif;color:var(--teal);line-height:1}
.logo .sub{font:9px 'Playfair Display',serif;color:#888;margin-left:22px}
.nav{top:33px;font:9px 'Playfair Display',serif;color:#333;letter-spacing:.3px}
.search{left:863px;top:25px;width:183px;height:24px;border:1px solid #e4e4e4;border-radius:12px;font-size:9px;color:#bbb;padding:6px 10px}
.search svg{position:absolute;right:8px;top:6px}
/* banners */
.bannerline{left:157px;top:133px;width:889px;height:2px;background:#444}
.banner{top:141px;height:116px;overflow:hidden}
.banner .photo{position:absolute;top:0;right:0;height:116px}
.banner-night{left:157px;width:434px;background:linear-gradient(90deg,#1c1626,#2b2236)}
.banner-night .photo{width:230px;background:linear-gradient(90deg,#2a2234,#5a4a58 60%,#3a3040)}
.banner-night h2{position:absolute;left:24px;top:36px;font:900 28px 'Playfair Display',serif;color:#fff;letter-spacing:1px}
.banner-night .shop{position:absolute;left:72px;top:76px;font:600 12px 'Open Sans',sans-serif;color:#fff;border-bottom:1px solid #aaa;padding-bottom:3px}
.banner-couture{left:613px;width:433px;background:linear-gradient(90deg,#0d2a2c,#16403f)}
.banner-couture .photo{width:130px;background:linear-gradient(90deg,#1a3a38,#6a4a3a 60%,#3a2a20)}
.banner-couture h2{position:absolute;left:14px;top:20px;font:400 44px 'Playfair Display',serif;color:#fff}
.banner-couture h2 small{font-size:14px;vertical-align:10px;margin-right:4px}
.banner-couture .tagline{position:absolute;left:105px;top:80px;font:italic 12px 'Playfair Display',serif;color:#cfe}
/* panels */
.panel{background:#fff}
.ptitle{position:absolute;left:12px;top:11px;font:700 12px 'Playfair Display',serif;color:#333;letter-spacing:.3px}
.ptitle span{color:var(--teal)}
.ptitle::after{content:"";position:absolute;left:0;top:22px;width:48px;height:3px;background:var(--teal)}
.pline{position:absolute;left:0;top:35px;right:0;height:1px;background:var(--line)}
.arrows{position:absolute;right:10px;top:12px;display:flex;gap:4px}
.arrows i{width:15px;height:15px;border:1px solid #999;border-radius:50%;font:normal 10px/12px sans-serif;text-align:center;color:#555}
/* product cards */
.grid{position:absolute;left:0;top:36px;display:grid}
.card{position:relative;height:395px;border-right:1px solid var(--line);border-bottom:1px solid var(--line);text-align:center;overflow:hidden}
.card .shot{position:absolute;left:10px;right:10px;top:0;height:280px;background:radial-gradient(ellipse 28% 48% at 50% 55%,#e9cdb8,#f6eee8 70%,#fbf9f8)}
.shot.pink{background:radial-gradient(ellipse 28% 48% at 50% 55%,#e7a0c0,#f3ddd6 70%,#fbf8f7)}
.shot.navy{background:radial-gradient(ellipse 28% 48% at 50% 55%,#9096b0,#eddcd0 70%,#fbf9f8)}
.shot.grey{background:radial-gradient(ellipse 28% 48% at 50% 55%,#b9bcc6,#efe3da 70%,#fbf9f8)}
.shot.red{background:radial-gradient(ellipse 28% 48% at 50% 55%,#d77a86,#f1dbd6 70%,#fbf8f7)}
.shot.white{background:radial-gradient(ellipse 28% 48% at 50% 55%,#f1e6de,#f3e4da 70%,#fbf9f8)}
.shot.blue{background:radial-gradient(ellipse 28% 48% at 50% 55%,#6a8fd6,#ecd8cc 70%,#fbf9f8)}
.shot.black{background:radial-gradient(ellipse 28% 48% at 50% 55%,#4a3a38,#d9b9a4 70%,#fbf9f8)}
.badge{position:absolute;right:14px;font:700 9px/11px 'Roboto',sans-serif;padding:2px 5px;background:#fff;border:1px solid #222;color:#222;white-space:nowrap}
.badge.new{border-color:var(--red);color:var(--red)}
.badge.pos1{top:12px}.badge.pos2{top:39px}
.card h3{position:absolute;left:14px;right:14px;top:298px;font:400 10.5px/14px 'Playfair Display',serif;color:#333;text-transform:uppercase}
.stars{position:absolute;left:0;right:0;top:330px;font-size:9px;color:var(--star);letter-spacing:1px}
.stars em{font-style:normal;color:#ccc}
.price{position:absolute;left:0;right:0;top:359px;font:12px 'Roboto',sans-serif;color:var(--red)}
.price s{color:#999;margin-right:3px}
/* tshirt banner */
.tshirt{left:157px;top:1128px;width:661px;height:233px;background:linear-gradient(90deg,#b6b29c,#cfcbb8 55%,#bdb8a4)}
.tshirt .photo{position:absolute;right:0;top:0;width:320px;height:233px;background:radial-gradient(ellipse 30% 45% at 55% 70%,#d957a0,#d9c9ae 60%,#c8c3ae)}
.tshirt h2{position:absolute;left:49px;top:70px;font:800 37px 'Open Sans',sans-serif;color:#222;letter-spacing:.5px}
.tshirt p{position:absolute;left:180px;top:118px;font:11px 'Roboto',sans-serif;color:#222}
.btn{position:absolute;background:var(--teal);color:#fff;font:700 9px 'Roboto',sans-serif;text-align:center}
/* sidebar */
.cats{left:841px;top:1128px;width:205px;height:419px}
.cats .head{height:40px;background:var(--teal);color:#fff;font:700 12px/40px 'Playfair Display',serif;text-align:center}
.cats li{list-style:none;height:38px;border-bottom:1px solid var(--line);display:flex;align-items:center;padding-left:12px;gap:14px;font:9.5px 'Playfair Display',serif;color:#333;text-transform:uppercase}
.cats li svg{flex:none}
.deals{left:841px;top:1570px;width:205px;height:470px;border-bottom:3px solid var(--teal)}
.deals .ptitle span{color:var(--red)}
.deals .ptitle::after{background:var(--red)}
.count{position:absolute;left:0;right:0;top:424px;height:40px;display:grid;grid-template-columns:repeat(4,1fr);border-top:1px solid var(--line)}
.count div{border-right:1px solid var(--line);text-align:center;padding-top:8px;font:700 11px 'Roboto',sans-serif;color:#222}
.count div small{display:block;font:400 7px 'Roboto',sans-serif;color:#888;margin-top:2px}
.peace{left:841px;top:2063px;width:205px;height:164px;overflow:hidden}
.peace .ghost{position:absolute;left:95px;top:20px;font:900 56px 'Open Sans',sans-serif;color:#f5f5f5;transform:rotate(45deg);z-index:0}
.peace h4,.peace h5,.peace p,.peace .amt,.peace .seal{z-index:1}
.peace h4{position:absolute;left:15px;top:12px;font:400 22px/22px 'Playfair Display',serif;color:var(--teal)}
.peace h5{position:absolute;left:15px;top:72px;font:700 13px 'Playfair Display',serif;color:#555}
.peace p{position:absolute;left:15px;top:93px;font:9.5px/12px 'Roboto',sans-serif;color:#555}
.peace .amt{position:absolute;left:13px;top:118px;font:700 26px 'Playfair Display',serif;color:var(--red)}
.peace .amt sup{font-size:13px}
.seal{position:absolute;left:134px;top:88px}
/* features */
.features{left:157px;top:2250px;width:889px;height:189px;display:grid;grid-template-columns:repeat(4,1fr)}
.feat{border-right:1px dashed #e0e0e0;position:relative;text-align:left}
.feat svg{position:absolute;left:50%;top:28px;transform:translateX(-50%)}
.feat h4{position:absolute;left:12px;top:98px;font:400 11px 'Playfair Display',serif;color:#333;white-space:nowrap}
.feat p{position:absolute;left:12px;right:12px;top:120px;font:300 9px/14px 'Roboto',sans-serif;color:#aaa}
/* color strip */
.strip{left:157px;top:2464px;width:889px;height:34px;display:grid;grid-template-columns:repeat(4,1fr)}
/* footer */
.footer{left:157px;top:2498px;width:889px;height:456px;background:var(--footer);color:#ddd}
.fcol{position:absolute;width:200px}
.fcol h4{font:700 10.5px 'Playfair Display',serif;color:#fff;letter-spacing:.2px;margin-bottom:18px}
.fcol li{list-style:none;font:9.5px/13.7px 'Roboto',sans-serif;color:#ccc}
.fdiv{position:absolute;left:18px;right:18px;top:208px;height:1px;background:#444}
.fbrand{font:700 20px 'Playfair Display',serif;color:#fff;display:flex;align-items:center;gap:6px}
.fbrand i{width:20px;height:20px;background:var(--teal);display:inline-block}
.ftext{font:9.5px/13px 'Roboto',sans-serif;color:#ccc;margin-top:22px}
.cards{display:grid;grid-template-columns:repeat(4,36px);gap:14px 9px}
.cards i{height:22px;background:#fff;border-radius:2px;display:block}
.nl p{font:9.5px/13px 'Roboto',sans-serif;color:#ddd;margin-bottom:14px}
.nl .field{display:flex;height:26px}
.nl .field span{flex:1;background:#2c2c2c;font:9px/26px 'Roboto',sans-serif;color:#777;padding-left:9px}
.nl .field b{width:55px;background:var(--teal);color:#fff;font:700 9px/26px 'Roboto',sans-serif;text-align:center}
.loc li{display:flex;gap:10px;align-items:center;margin-bottom:10px;line-height:13px}
.copy{position:absolute;left:0;right:0;top:398px;text-align:center;font:9.5px/16px 'Roboto',sans-serif;color:#ccc}
.copy span{color:var(--teal)}
</style>
</head>
<body>

<!-- Top bar -->
<div class="abs topbar">
  <div class="abs welcome">Welcome visitor! you can <b>login</b> or <b>create an account</b></div>
  <div class="abs sep" style="left:383px"></div>
  <div class="abs menu" style="left:395px">▪ ENGLISH ⌄</div>
  <div class="abs sep" style="left:470px"></div>
  <div class="abs menu" style="left:486px">ACCOUNT ⌄</div>
  <div class="abs sep" style="left:552px"></div>
  <div class="abs cart">
    <svg width="24" height="18" viewBox="0 0 24 18"><path d="M1 2h4l3 10h12l3-8H7" fill="none" stroke="#fff" stroke-width="2"/><circle cx="10" cy="16" r="1.6" fill="#fff"/><circle cx="18" cy="16" r="1.6" fill="#fff"/></svg>
    <div class="t1">SHOPPING CART</div>
    <div class="t2">0 item(s) - $0.00 ⌄</div>
  </div>
</div>

<!-- Header -->
<div class="abs header">
  <div class="abs logo"><div class="name">VelvetCrate</div><div class="sub">online store</div></div>
  <div class="abs nav" style="left:325px">HOME</div>
  <div class="abs nav" style="left:386px">CATEGORIES ⌄</div>
  <div class="abs nav" style="left:479px">ACCESSORIES ⌄</div>
  <div class="abs nav" style="left:575px">SERVICES</div>
  <div class="abs nav" style="left:652px">SUPPORT</div>
  <div class="abs nav" style="left:727px">BLOGS</div>
  <div class="abs nav" style="left:791px">CONTACT</div>
  <div class="abs search">Search...
    <svg width="10" height="10" viewBox="0 0 10 10"><circle cx="4" cy="4" r="3" fill="none" stroke="#999"/><path d="M6.5 6.5L9 9" stroke="#999"/></svg>
  </div>
</div>

<!-- Promo banners -->
<div class="abs bannerline"></div>
<div class="abs" style="left:758px;top:133px;width:230px;height:2px;background:var(--teal)"></div>
<div class="abs" style="left:988px;top:133px;width:58px;height:2px;background:#e8833a"></div>
<div class="abs banner banner-night">
  <div class="photo" role="img" aria-label="Model in satin nightwear lying on dark sheets"></div>
  <h2>NIGHTWEAR</h2>
  <div class="shop">SHOP NOW</div>
</div>
<div class="abs banner banner-couture">
  <div class="photo" role="img" aria-label="Portrait of a model with long wavy hair"></div>
  <h2><small>Velour</small>couture</h2>
  <div class="tagline">Sexy Lingerie &amp; Swimwear</div>
</div>

<!-- Featured products -->
<section class="abs panel" style="left:157px;top:280px;width:889px;height:826px">
  <div class="ptitle"><span>FEATURED</span> PRODUCTS</div>
  <div class="arrows"><i>‹</i><i>›</i></div>
  <div class="pline"></div>
  <div class="grid" style="grid-template-columns:repeat(4,222.25px)">
    <div class="card"><div class="shot navy" role="img" aria-label="Model in navy print bikini"></div><span class="badge pos1">SALE</span><span class="badge new pos2">NEW</span><h3>Culpa qui officia deserunt lorem ipsum</h3><div class="stars">★★★<em>★★</em></div><div class="price"><s>$280.00</s>$215.00</div></div>
    <div class="card"><div class="shot navy" role="img" aria-label="Model in striped bandeau bikini"></div><span class="badge new pos1">NEW</span><h3>Excepteur sint occaecat cupidatat non proident</h3><div class="stars">★★★<em>★★</em></div><div class="price">$235.00</div></div>
    <div class="card"><div class="shot pink" role="img" aria-label="Model in pink lace bra set"></div><span class="badge new pos1">NEW</span><h3>Quis autem vel eum iure reprehenderit</h3><div class="stars">★★★★<em>★</em></div><div class="price">$160.00</div></div>
    <div class="card"><div class="shot grey" role="img" aria-label="Model in grey tank and shorts"></div><span class="badge new pos1">NEW</span><h3>Nemo enim ipsam voluptatem quia voluptas</h3><div class="stars"><em>★★★★★</em></div><div class="price">$190.00</div></div>
    <div class="card"><div class="shot pink" role="img" aria-label="Model in pink lace lingerie"></div><span class="badge new pos1">NEW</span><h3>Esse cillum dolore eu</h3><div class="stars">★★★<em>★★</em></div><div class="price">$215.00</div></div>
    <div class="card"><div class="shot red" role="img" aria-label="Model in coral lace lingerie"></div><span class="badge new pos1">NEW</span><h3>Quis nostrud exercitation</h3><div class="stars"><em>★★★★★</em></div><div class="price">$190.00</div></div>
    <div class="card"><div class="shot pink" role="img" aria-label="Model in magenta bra set"></div><span class="badge pos1">SALE</span><h3>Voluptatem accusantium</h3><div class="stars">★★★<em>★★</em></div><div class="price"><s>$190.00</s>$178.00</div></div>
    <div class="card"><div class="shot grey" role="img" aria-label="Model in grey loungewear"></div><h3>Reprehenderit in voluptate</h3><div class="stars">★★★<em>★★</em></div><div class="price">$118.00</div></div>
  </div>
</section>

<!-- T-shirt banner -->
<div class="abs tshirt">
  <div class="photo" role="img" aria-label="Model wearing a pink patterned halter top"></div>
  <h2>T-SHIRT DESIGN</h2>
  <p>Women's One Shoulder Shirred</p>
  <div class="btn" style="left:225px;top:152px;width:107px;height:29px;line-height:29px">VIEW COLLECTION</div>
</div>

<!-- Categories sidebar -->
<aside class="abs panel cats">
  <div class="head">☰ SHOP BY CATEGORIES</div>
  <ul>
    <li><svg width="12" height="10"><rect x="1" y="2" width="10" height="7" fill="none" stroke="#666"/><circle cx="6" cy="5.5" r="2" fill="#666"/></svg>Camera &amp; Camcorders</li>
    <li><svg width="12" height="10"><rect x="1" y="1" width="10" height="8" fill="none" stroke="#666"/><path d="M3 1v8M9 1v8" stroke="#666"/></svg>Entertaiment</li>
    <li><svg width="12" height="10"><rect x="2" y="1" width="8" height="6" fill="none" stroke="#666"/><path d="M0 9h12" stroke="#666"/></svg>Computer</li>
    <li><svg width="12" height="10"><rect x="3" y="0" width="6" height="10" rx="1" fill="none" stroke="#666"/></svg>Smartphones</li>
    <li><svg width="12" height="10"><rect x="1" y="3" width="10" height="7" fill="#666"/><rect x="5" y="0" width="2" height="10" fill="#fff"/></svg>Gift box</li>
    <li><svg width="12" height="10"><rect x="0" y="2" width="12" height="6" rx="3" fill="#666"/></svg>Game &amp; Software</li>
    <li><svg width="12" height="10"><path d="M4 8V1l7-1v7" fill="none" stroke="#666"/><circle cx="3" cy="8" r="2" fill="#666"/><circle cx="10" cy="7" r="2" fill="#666"/></svg>Audio devices</li>
    <li><svg width="12" height="10"><path d="M1 4h3l6-3v8L4 6H1z" fill="#666"/></svg>Safety equipment</li>
    <li><svg width="12" height="10"><rect x="1" y="2" width="10" height="8" fill="#666"/></svg>Hammers</li>
    <li><svg width="12" height="10"><circle cx="4" cy="4" r="3" fill="none" stroke="#666" stroke-width="1.5"/><circle cx="9" cy="8" r="2" fill="none" stroke="#666"/></svg>Handsaws</li>
  </ul>
</aside>

<!-- Latest products -->
<section class="abs panel" style="left:157px;top:1384px;width:661px;height:822px">
  <div class="ptitle"><span>LATEST</span> PRODUCTS</div>
  <div class="pline"></div>
  <div class="grid" style="grid-template-columns:repeat(3,220.33px)">
    <div class="card"><div class="shot white" role="img" aria-label="Model in white bikini"></div><h3>Dolores eos qui ratione voluptatem sequi nesciunt</h3><div class="stars">★★★★<em>★</em></div><div class="price">$186.00</div></div>
    <div class="card"><div class="shot pink" role="img" aria-label="Model in magenta bra set"></div><span class="badge pos1">SALE</span><h3>Voluptatem accusantium</h3><div class="stars">★★★<em>★★</em></div><div class="price"><s>$190.00</s>$178.00</div></div>
    <div class="card"><div class="shot grey" role="img" aria-label="Model in grey loungewear"></div><h3>Reprehenderit in voluptate</h3><div class="stars">★★★<em>★★</em></div><div class="price">$118.00</div></div>
    <div class="card"><div class="shot white" role="img" aria-label="Model in ivory lace lingerie"></div><span class="badge pos1">SALE</span><h3>Ullamco laboris nisi ut aliquip</h3><div class="stars">★★★<em>★★</em></div><div class="price"><s>$220.00</s>$215.00</div></div>
    <div class="card"><div class="shot blue" role="img" aria-label="Model in blue floral lingerie"></div><span class="badge pos1">SALE</span><h3>Neque porro quisquam</h3><div class="stars"><em>★★★★★</em></div><div class="price"><s>$196.00</s>$182.00</div></div>
    <div class="card"><div class="shot black" role="img" aria-label="Model in black floral lingerie"></div><span class="badge pos1">SALE</span><h3>Cupidatat non proident</h3><div class="stars">★★★<em>★★</em></div><div class="price"><s>$215.00</s>$205.00</div></div>
  </div>
</section>

<!-- Deals of the day -->
<aside class="abs panel deals">
  <div class="ptitle"><span>DEALS OF</span> THE DAY!</div>
  <div class="pline"></div>
  <div class="card" style="position:absolute;left:0;top:36px;width:205px;height:388px;border:0">
    <div class="shot navy" role="img" aria-label="Model in navy print bikini"></div>
    <span class="badge pos1">SAVE 23%</span><span class="badge new pos2">NEW</span>
    <h3>Culpa qui officia deserunt lorem ipsum</h3>
    <div class="stars">★★★<em>★★</em></div>
    <div class="price"><s>$280.00</s>$215.00</div>
  </div>
  <div class="count"><div>508<small>Days</small></div><div>09<small>Hours</small></div><div>27<small>Mins</small></div><div style="border:0">49<small>Secs</small></div></div>
</aside>

<!-- Warranty promo -->
<aside class="abs panel peace">
  <div class="ghost">SALE</div>
  <h4>PEACE OF<br>MIND</h4>
  <h5>EXTENDED WARRANTIES</h5>
  <p>Available for<br>3 - 5 years from</p>
  <div class="amt"><sup>$</sup>26.00</div>
  <svg class="seal" width="74" height="74" viewBox="0 0 74 74"><circle cx="37" cy="37" r="36" fill="var(--teal)"/><path d="M22 34l10 10 20-22" fill="none" stroke="#fff" stroke-width="6"/><text x="37" y="60" fill="#fff" font-family="Roboto" font-weight="700" font-size="7" text-anchor="middle">WARRANTIES</text></svg>
</aside>

<!-- Service features -->
<div class="abs panel features">
  <div class="feat">
    <svg width="46" height="36" viewBox="0 0 46 36"><rect x="7" y="3" width="32" height="22" rx="2" fill="none" stroke="#444" stroke-width="3"/><path d="M1 30h44v3H1z" fill="#444"/></svg>
    <h4>RESERVE ONLINE &amp; COLLECT</h4><p>Duis sed odio sit amet nibh odio tincidunt vitae auctor eu in elit.</p></div>
  <div class="feat">
    <svg width="46" height="36" viewBox="0 0 46 36"><rect x="14" y="4" width="30" height="22" fill="#444"/><path d="M2 26V16l6-8h8v18z" fill="#444"/><circle cx="10" cy="29" r="4" fill="#444" stroke="#fff" stroke-width="2"/><circle cx="36" cy="29" r="4" fill="#444" stroke="#fff" stroke-width="2"/></svg>
    <h4>FREE DELIVERY ON ALL ORDERS</h4><p>Duis sed odio sit amet nibh odio tincidunt vitae auctor eu in elit.</p></div>
  <div class="feat">
    <svg width="46" height="40" viewBox="0 0 46 40"><path d="M18 4l6 0 8 13-5 3M38 24l4 7-6 6h-10M14 37H6l-4-7 6-11" fill="none" stroke="#444" stroke-width="6" stroke-linejoin="round"/></svg>
    <h4>FREE RECYCLING ON ALL PRODUCT</h4><p>Duis sed odio sit amet nibh odio tincidunt vitae auctor eu in elit.</p></div>
  <div class="feat" style="border:0">
    <svg width="46" height="42" viewBox="0 0 46 42"><path d="M8 38L26 20" stroke="#444" stroke-width="7" stroke-linecap="round"/><path d="M24 14a10 10 0 0 1 14-10l-6 6 2 6 6 2 6-6a10 10 0 0 1-10 14z" fill="#444"/></svg>
    <h4>WE CAN INSTALL</h4><p>AND SUPPORT YOUR NEW PRODUCT AFTER YOU BUY</p></div>
</div>

<!-- Colour strip -->
<div class="abs strip"><i style="background:var(--fb)"></i><i style="background:var(--tw)"></i><i style="background:var(--gr)"></i><i style="background:var(--rd)"></i></div>

<!-- Footer -->
<footer class="abs footer">
  <div class="fcol" style="left:18px;top:38px"><h4>POPULAR SEARCHES</h4><ul><li>Dorvane</li><li>Soundbar</li><li>Solmara HX8500</li><li>Tonelo</li><li>Fridge Freezer</li><li>TV</li><li>Washing Machine</li><li>Dishwasher</li></ul></div>
  <div class="fcol" style="left:237px;top:38px"><h4>SHOP BY BRANDS</h4><ul><li>Brennik</li><li>Dorvane</li><li>Heatwise</li><li>Lumo</li><li>Panterra</li><li>Rangecraft</li><li>Solmara</li><li>Zavelli</li></ul></div>
  <div class="fcol" style="left:456px;top:38px"><h4>SHOP BY CATEGORIES</h4><ul><li>Cookers</li><li>Hobs</li><li>Irons</li><li>Laundry</li><li>Speakers</li><li>Vacuum Cleaners</li><li>Televisions</li><li>Small Appliances</li></ul></div>
  <div class="fcol" style="left:675px;top:38px"><h4>CAN WE HELP?</h4><ul><li>Help Center</li><li>Track Your Order</li><li>About Us</li><li>Our Location</li><li>Contact Us</li><li>Archive Template</li><li>Our Company</li></ul></div>
  <div class="fdiv"></div>
  <div class="fcol" style="left:18px;top:232px;width:200px"><div class="fbrand"><i></i>VelvetCrate</div><p class="ftext">Lorem ipsum dolor sit amet, consectetuer adipiscing elit. Aenean commodo ligula felis, ultricies nec, pellentesque eu, tium quis, sem.</p></div>
  <div class="fcol" style="left:237px;top:239px"><h4>PAYMENT METHODS</h4><div class="cards"><i></i><i></i><i></i><i></i><i></i><i></i><i></i><i></i></div></div>
  <div class="fcol nl" style="left:456px;top:239px;width:195px"><h4>NEWSLETTER</h4><p>Sign up for our new letter for exclusive updates on contests, new products, and more.</p><div class="field"><span>Your email...</span><b>SUBMIT</b></div></div>
  <div class="fcol loc" style="left:675px;top:239px"><h4>STORE LOCATION</h4><ul>
    <li><svg width="10" height="13" viewBox="0 0 10 13"><path d="M5 13S0 7 0 5a5 5 0 0 1 10 0c0 2-5 8-5 8z" fill="#ddd"/><circle cx="5" cy="5" r="2" fill="#353535"/></svg>No 48, Linden Court, Ashford, USA</li>
    <li><svg width="12" height="12" viewBox="0 0 12 12"><circle cx="6" cy="6" r="5.3" fill="none" stroke="#ddd"/><path d="M4 3l1 2-1 1 2 2 1-1 2 1-1 2C6 10 2 6 2 4z" fill="#ddd"/></svg>Phone: (+1) 0555 014 782</li>
    <li><svg width="13" height="10" viewBox="0 0 13 10"><rect x=".5" y=".5" width="12" height="9" fill="none" stroke="#ddd"/><path d="M.5.5l6 5 6-5" fill="none" stroke="#ddd"/></svg>Email: info@velvetcrate.shop</li>
  </ul></div>
  <div class="copy">Copyright 2016 Demo Store. All Rights Reserved.<br>Developed By <span>DEMO THEME</span></div>
</footer>

</body>
</html>
```